Property Report

8 page document, similar theme to our website (www.harbourandvale.example) and previous brochure (provided). All content provided. We want a professional looking document. We need ASAP. Thanks!

Industry/Entity Type

Property

Font styles to use
Serif
Sans Serif

Colors
ffc214
ffcf3e
fee18a
fff3d1

Requirements
Must have
• Page 1: Cover
Page 2: Content
Page 3: About Us
Page 4: Site Description
Page 5: Scheme
Page 6: Analysis
Page 7: Conclusion
Page 8: Contact Details

```html
<!DOCTYPE html>
<html lang="en">
<head>
<meta charset="utf-8">
<title>Site Description</title>
<link href="https://fonts.googleapis.com/css2?family=Roboto:wght@300;700&display=swap" rel="stylesheet">
<style>
  :root {
    --band-grey: #676b6f;
    --accent: #f7a21b;
    --white: #ffffff;
    --map-base: #ecdcb4;
    --map-warm: #fcd9a8;
  }
  * { margin: 0; padding: 0; box-sizing: border-box; }
  html, body { width: 848px; height: 1200px; overflow: hidden; background: var(--white); }
  .page { position: relative; width: 848px; height: 1200px; font-family: 'Roboto', sans-serif; }
  .intro-band {
    position: absolute; left: 0; top: 0; width: 848px; height: 423px;
    background: var(--band-grey); padding: 92px 81px 0 81px;
  }
  .section-title {
    color: var(--accent); font-weight: 700; font-size: 38.5px; line-height: 1;
    letter-spacing: -0.2px;
  }
  .title-rule { width: 72px; height: 10px; background: var(--white); margin: 14px 0 23px; }
  .intro-text p {
    color: var(--white); font-weight: 300; font-size: 16.6px; line-height: 20.6px;
    margin-bottom: 13px; width: 690px;
  }
  .site-plan {
    position: absolute; left: 81px; top: 477px; width: 691px; height: 415px;
    background: linear-gradient(135deg, var(--map-warm) 0%, var(--map-base) 55%, #e4e6d8 100%);
  }
  .page-number {
    position: absolute; left: 81px; top: 1150px; width: 40px; height: 50px;
    background: var(--band-grey); color: var(--white); font-weight: 300;
    font-size: 20px; text-align: center; padding-top: 7px;
  }
</style>
</head>
<body>
<div class="page">
  <section class="intro-band">
    <h1 class="section-title">Site Description</h1>
    <div class="title-rule"></div>
    <div class="intro-text">
      <p>Harbour and Vale Commercial have been asked by Daniel Marsh the representative for Marsh Holdings Limited to advise on the best disposal method to maximise value for their property.</p>
      <p>The existing property measures approximately 9,655 square feet internally with parking spaces.</p>
      <p>The site was granted permitted development rights in 2016 to be converted into 11 flats and 11 parking spaces but this was no implemented.</p>
      <p>We understand that the vendors operate their business from the premises and the property has a designated use class of B1(a) Office/E Class.</p>
    </div>
  </section>
  <div class="site-plan" role="img" aria-label="Site location plan showing the property boundary outlined in red among surrounding streets and buildings"></div>
  <div class="page-number">4</div>
</div>
</body>
</html>
```